Copperleaf Motorized Shade Business Card

Hello, we've had our logo made. Now we are looking for a clean and cool looking business card. One side can just be the logo with any design elements that might look good with it. The other side will be Name, Phone Number and Email. There will not be an address on the card.

```html
<!DOCTYPE html>
<html lang="en">
<head>
<meta charset="UTF-8">
<title>Copperleaf Motorized Shades – Business Card</title>
<link rel="stylesheet" href="https://fonts.googleapis.com/css2?family=Barlow+Condensed:wght@600&family=Poppins:wght@300;400&display=swap">
<style>
  :root {
    --page-bg: #e9eaec;
    --card-navy: #1b3a72;
    --card-navy-deep: #173163;
    --panel-soft: #27478a;
    --name-blue: #2a9fd8;
    --accent-gold: #e8b020;
    --text-white: #f4f6fa;
    --logo-silver: #d9dde4;
  }
  * { margin: 0; padding: 0; box-sizing: border-box; }
  html, body {
    width: 1200px; height: 900px; overflow: hidden;
    background: var(--page-bg);
  }
  .canvas {
    width: 1200px; height: 900px;
    display: flex; flex-direction: column;
    align-items: center; justify-content: center; gap: 40px;
  }
  .card {
    width: 700px; height: 400px;
    background: var(--card-navy);
    position: relative; overflow: hidden;
    box-shadow: 0 6px 18px rgba(0,0,0,0.18);
  }
  /* Contact side */
  .contact-block {
    position: absolute; left: 0; right: 0; top: 50%;
    transform: translateY(-50%);
    display: flex; align-items: center; justify-content: center; gap: 26px;
  }
  .identity { text-align: right; }
  .identity__name {
    font-family: "Barlow Condensed", sans-serif; font-weight: 600;
    font-size: 40px; letter-spacing: 1px; line-height: 1;
    color: var(--name-blue); text-transform: uppercase;
  }
  .identity__title {
    font-family: "Poppins", sans-serif; font-weight: 300;
    font-size: 15px; color: var(--text-white); margin-top: 2px;
  }
  .divider {
    width: 2px; height: 62px; background: var(--accent-gold);
    transform: skewX(-20deg);
  }
  .details { font-family: "Poppins", sans-serif; color: var(--text-white); }
  .details__row { display: flex; align-items: center; gap: 8px; }
  .details__row svg { flex: none; }
  .details__phone { font-size: 22px; font-weight: 300; letter-spacing: 0.5px; }
  .details__email { font-size: 13px; font-weight: 300; margin-top: 4px; }
  /* Logo side */
  .card--brand { background: var(--card-navy-deep); }
  .brand-backdrop {
    position: absolute; inset: 0;
    background: radial-gradient(circle at 62% 58%, var(--panel-soft) 0, var(--panel-soft) 30%, transparent 31%);
    opacity: 0.7;
  }
  .brand-mark {
    position: absolute; inset: 0;
    display: flex; flex-direction: column; align-items: center; justify-content: center;
    font-family: "Barlow Condensed", sans-serif; font-weight: 600;
    color: var(--logo-silver); text-transform: uppercase; text-align: center;
  }
  .brand-mark__name { font-size: 64px; letter-spacing: 3px; line-height: 1; }
  .brand-mark__tag { font-size: 18px; letter-spacing: 7px; margin-top: 8px; }
</style>
</head>
<body>
<main class="canvas">
  <section class="card card--contact">
    <div class="contact-block">
      <div class="identity">
        <div class="identity__name">Daniel Reyes</div>
        <div class="identity__title">President</div>
      </div>
      <div class="divider"></div>
      <div class="details">
        <div class="details__row details__phone">
          <svg width="12" height="14" viewBox="0 0 12 14" aria-hidden="true"><path d="M3 1 L5 4 L3.5 5.5 C4.5 8 6 9.5 8 10.5 L9.5 9 L12 11 L10 13.5 C5 12.5 1 8 0.5 3 Z" fill="var(--name-blue)"/></svg>
          <span>(470) 555-0142</span>
        </div>
        <div class="details__row details__email">
          <svg width="14" height="10" viewBox="0 0 14 10" aria-hidden="true"><rect x="0" y="0" width="14" height="10" fill="var(--name-blue)"/><path d="M0 0 L7 6 L14 0" fill="none" stroke="var(--card-navy)" stroke-width="1.2"/></svg>
          <span>d.reyes@copperleafmail.com</span>
        </div>
      </div>
    </div>
  </section>
  <section class="card card--brand">
    <div class="brand-backdrop" role="img" aria-label="Faint brand decoration area"></div>
    <div class="brand-mark">
      <div class="brand-mark__name">Copperleaf</div>
      <div class="brand-mark__tag">Motorized Shades</div>
    </div>
  </section>
</main>
</body>
</html>
```